Qorvane Management LLC Business Card

The sample logo was attached for the business Card Design for Traffic Control Company named Qorvane Management LLC. Card design needs to have the company logo and colors match the logo color. It will be nice to show some images of Traffic control signs or cones, even roads closer that math the company services

Target Market(s)

Temporary traffic control. Road closer.

Industry/Entity Type

Construction

Contact Information for Business Card

basic information, name, job title, address, email phone, website

Font styles to use
Serif
Sans Serif

Colors
F0912C
F2A743
F7CA91
FBE8D2
FDF5EE
EE7325
F08F49
F5BC92
FAE3D3
FDF4ED

```html
<!DOCTYPE html>
<html lang="en">
<head>
<meta charset="utf-8">
<title>Qorvane Management LLC – Business Card</title>
<link rel="stylesheet" href="https://fonts.googleapis.com/css2?family=Montserrat:wght@400;500;700&display=swap">
<style>
  :root {
    --page-bg: #1c1c1c;
    --card-white: #ffffff;
    --card-dark: #4b4b4b;
    --band-grey: #4a4a4a;
    --brand-orange: #ee7325;
    --text-dark: #3a3a3a;
    --emboss-grey: #6b6b6b;
  }
  html, body {
    margin: 0;
    padding: 0;
    width: 1200px;
    height: 900px;
    overflow: hidden;
    background: var(--page-bg);
    font-family: "Montserrat", sans-serif;
  }
  .canvas {
    position: relative;
    width: 1200px;
    height: 900px;
  }
  .card {
    position: absolute;
    left: 320px;
    width: 560px;
    height: 320px;
    border-radius: 22px;
    overflow: hidden;
  }
  .card-back {
    top: 100px;
    background: var(--card-dark);
    display: flex;
    flex-direction: column;
    align-items: center;
    justify-content: center;
  }
  .back-name {
    color: var(--emboss-grey);
    font-weight: 700;
    text-align: center;
    line-height: 1.05;
  }
  .back-name .name-main { display: block; font-size: 64px; letter-spacing: 1px; }
  .back-name .name-sub { display: block; font-size: 20px; letter-spacing: 4px; text-transform: uppercase; margin-top: 6px; }

  .card-front {
    top: 480px;
    background: var(--card-white);
  }
  .front-band {
    position: absolute;
    inset: 0;
    width: 560px;
    height: 320px;
  }
  .front-brand {
    position: absolute;
    left: 34px;
    top: 100px;
    width: 230px;
    color: var(--brand-orange);
    font-weight: 700;
    line-height: 1.05;
  }
  .front-brand .name-main { display: block; font-size: 46px; }
  .front-brand .name-sub { display: block; font-size: 14px; letter-spacing: 3px; text-transform: uppercase; margin-top: 6px; }
  .divider {
    position: absolute;
    left: 278px;
    top: 82px;
    width: 2px;
    height: 150px;
    background: var(--brand-orange);
  }
  .contact {
    position: absolute;
    left: 298px;
    top: 76px;
    color: var(--text-dark);
    font-size: 13px;
    line-height: 1.45;
  }
  .contact .person { color: var(--brand-orange); font-weight: 700; font-size: 23px; letter-spacing: 0.5px; margin: 0; line-height: 1.1; }
  .contact .role { margin: 2px 0 8px; }
  .contact .address { margin: 0 0 6px; }
  .contact ul { list-style: none; margin: 0; padding: 0; }
  .contact li { display: flex; align-items: center; gap: 6px; }
  .contact svg { width: 11px; height: 11px; flex: none; }
</style>
</head>
<body>
<main class="canvas">
  <section class="card card-back" aria-label="Card back">
    <div class="back-name">
      <span class="name-main">Qorvane</span>
      <span class="name-sub">Management LLC</span>
    </div>
  </section>

  <section class="card card-front" aria-label="Card front">
    <svg class="front-band" viewBox="0 0 560 320" aria-hidden="true">
      <path d="M0 232 Q 60 238 110 252 Q 320 310 560 304 L560 320 L0 320 Z" fill="var(--band-grey)"/>
      <path d="M110 246 Q 320 302 560 296" fill="none" stroke="var(--brand-orange)" stroke-width="5"/>
    </svg>

    <div class="front-brand">
      <span class="name-main">Qorvane</span>
      <span class="name-sub">Management LLC</span>
    </div>

    <div class="divider"></div>

    <div class="contact">
      <p class="person">DANIEL REYES</p>
      <p class="role">CEO/Founder</p>
      <p class="address">2187 Halvern Avenue<br>Marlow Heights, CA 90518</p>
      <ul>
        <li>
          <svg viewBox="0 0 24 24"><path fill="var(--brand-orange)" d="M6.6 10.8a15.1 15.1 0 0 0 6.6 6.6l2.2-2.2a1 1 0 0 1 1-.25 11.4 11.4 0 0 0 3.6.57 1 1 0 0 1 1 1V20a1 1 0 0 1-1 1A17 17 0 0 1 3 4a1 1 0 0 1 1-1h3.5a1 1 0 0 1 1 1c0 1.25.2 2.45.57 3.57a1 1 0 0 1-.25 1z"/></svg>
          555-214-7390
        </li>
        <li>
          <svg viewBox="0 0 24 24"><rect x="2" y="5" width="20" height="14" rx="2" fill="none" stroke="var(--brand-orange)" stroke-width="2.4"/><path d="M3 6l9 7 9-7" fill="none" stroke="var(--brand-orange)" stroke-width="2.4"/></svg>
          info@qorvanemgmt.com
        </li>
        <li>
          <svg viewBox="0 0 24 24"><circle cx="12" cy="12" r="10" fill="none" stroke="var(--brand-orange)" stroke-width="2.2"/><path d="M2 12h20M12 2c3 3 3 17 0 20M12 2c-3 3-3 17 0 20" fill="none" stroke="var(--brand-orange)" stroke-width="1.8"/></svg>
          www.qorvanemgmt.com
        </li>
      </ul>
    </div>
  </section>
</main>
</body>
</html>
```